Data Analytics Irish company needs Stationery Design

We need a stationery design for our data analytics company based in Dublin called 'Numbryx': we develop innovative web-based corporate applications exploiting advanced Machine Learning and Data Mining techniques.
Like the animal that inspired our company name, the final design should communicate intelligence and passion; on the other hand, we want to keep the highest professional appeal.
We love our current logo and we have tried out several color variations: we prefer solutions (see the logo attached) with white design and dark backgrounds, but we will also be glad to see some designs that follow the colors of the palette of the attached web screenshot.

```html
<!DOCTYPE html>
<html lang="en">
<head>
<meta charset="utf-8">
<title>Numbryx Stationery</title>
<link href="https://fonts.googleapis.com/css2?family=Questrial&display=swap" rel="stylesheet">
<style>
  :root {
    --backdrop: #a6a6a6;
    --paper: #ffffff;
    --paper-shade: #f1f1f1;
    --charcoal: #2f2f2f;
    --charcoal-deep: #232323;
    --brand-blue: #3f6db5;
    --ink-grey: #5a5a5a;
    --wash-light: rgba(0, 0, 0, .075);
    --wash-dark: rgba(255, 255, 255, .055);
  }
  * { box-sizing: border-box; margin: 0; padding: 0; }
  html, body { width: 1200px; height: 974px; overflow: hidden; }
  body {
    background: radial-gradient(ellipse at 50% 45%, #b4b4b4 0%, var(--backdrop) 70%, #9a9a9a 100%);
    font-family: "Questrial", "Century Gothic", sans-serif;
    position: relative;
  }
  .piece { position: absolute; overflow: hidden; box-shadow: 0 2px 6px rgba(0,0,0,.18); }
  .light-paper { background: linear-gradient(170deg, var(--paper) 40%, var(--paper-shade) 100%); }
  .wordmark {
    display: flex; align-items: center; gap: 6px;
    position: absolute; color: var(--ink-grey); font-weight: 400; letter-spacing: .2px;
    z-index: 2;
  }
  .wordmark .dot { border-radius: 50%; background: var(--brand-blue); flex: none; }
  .on-dark .wordmark { color: #d4d4d4; }
  .decor-wash { position: absolute; }
  .light-paper .decor-wash { background: radial-gradient(closest-side, var(--wash-light) 0%, rgba(0,0,0,.04) 55%, transparent 100%); }
  .on-dark .decor-wash { background: radial-gradient(closest-side, var(--wash-dark) 0%, rgba(255,255,255,.03) 55%, transparent 100%); }

  /* letterhead */
  .letterhead { left: 112px; top: 118px; width: 360px; height: 510px; }
  .letterhead .wordmark { left: 30px; top: 28px; font-size: 20px; }
  .letterhead .wordmark .dot { width: 22px; height: 22px; }
  .letterhead .address {
    position: absolute; right: 26px; top: 25px; text-align: right;
    font-size: 5.5px; line-height: 8px; color: #777;
  }
  .letterhead .address b { color: var(--brand-blue); }
  .letterhead .decor-wash { left: 20px; top: 150px; width: 340px; height: 290px; }
  .letterhead svg.footer { position: absolute; left: 0; bottom: 0; }

  /* folder */
  .folder { left: 515px; top: 117px; width: 360px; height: 511px; border-radius: 3px;
    background: radial-gradient(ellipse at 60% 20%, #3a3a3a, var(--charcoal-deep) 75%); }
  .folder .spine { position: absolute; left: 16px; top: 0; bottom: 0; width: 1px; background: #444; }
  .folder .wordmark { left: 130px; top: 52px; font-size: 27px; }
  .folder .wordmark .dot { width: 30px; height: 30px; }
  .folder .decor-wash { left: -20px; top: 140px; width: 360px; height: 400px; }

  /* business cards */
  .card-front { left: 112px; top: 670px; width: 154px; height: 87px; }
  .card-front .wordmark { left: 12px; top: 15px; font-size: 14px; }
  .card-front .wordmark .dot { width: 14px; height: 14px; }
  .card-front .contact { position: absolute; left: 10px; top: 61px; font-size: 4.5px; line-height: 6.5px; color: #bbb; }
  .card-front .contact i { display: inline-block; width: 4px; height: 4px; border-radius: 50%; background: var(--brand-blue); margin-right: 3px; vertical-align: middle; }
  .card-front .holder { position: absolute; right: 10px; top: 62px; text-align: right; color: #eee; font-size: 6px; }
  .card-front .holder small { display: block; font-size: 4.5px; color: #aaa; }
  .card-back { left: 112px; top: 773px; width: 154px; height: 85px; background: var(--charcoal); }
  .card-back .decor-wash { left: 10px; top: -5px; width: 110px; height: 95px; }
  .card-back .wordmark { left: 34px; top: 32px; font-size: 15px; }
  .card-back .wordmark .dot { width: 15px; height: 15px; }

  /* compliment slip */
  .slip { left: 308px; top: 682px; width: 360px; height: 169px; }
  .slip .wordmark { left: 22px; top: 20px; font-size: 18px; }
  .slip .wordmark .dot { width: 20px; height: 20px; }
  .slip .decor-wash { left: 165px; top: -10px; width: 180px; height: 150px; }
  .slip svg.footer { position: absolute; left: 0; bottom: 0; }
  .slip .address { position: absolute; left: 50px; bottom: 9px; font-size: 5px; color: #bbb; z-index: 2; }

  /* envelope */
  .envelope { left: 705px; top: 682px; width: 360px; height: 169px; }
  .envelope svg { position: absolute; left: 0; top: 0; }
  .envelope .seal-dot { position: absolute; left: 172px; top: 20px; width: 16px; height: 16px; border-radius: 50%; background: var(--brand-blue); }
</style>
</head>
<body>

  <section class="piece letterhead light-paper" aria-label="Letterhead">
    <div class="wordmark"><span class="dot"></span>Numbryx</div>
    <p class="address">Harbour Court<br>Ringsend, Dublin 4.<br><b>T:</b> 01-555-0182<br><b>E:</b> info@numbryx.com<br><b>W:</b> www.numbryx.com</p>
    <div class="decor-wash" role="img" aria-label="Faint brand symbol watermark"></div>
    <svg class="footer" width="360" height="40" viewBox="0 0 360 40">
      <path d="M0 14 Q160 4 360 22 L360 40 L0 40 Z" fill="var(--charcoal)"/>
      <path d="M0 9 Q160 -1 360 18" fill="none" stroke="var(--brand-blue)" stroke-width="3"/>
    </svg>
  </section>

  <section class="piece folder on-dark" aria-label="Presentation folder">
    <div class="spine"></div>
    <div class="decor-wash" role="img" aria-label="Faint brand symbol watermark"></div>
    <div class="wordmark"><span class="dot"></span>Numbryx</div>
  </section>

  <section class="piece card-front light-paper" aria-label="Business card front">
    <div class="wordmark"><span class="dot"></span>Numbryx</div>
    <svg width="154" height="87" viewBox="0 0 154 87" style="position:absolute;left:0;top:0">
      <path d="M0 50 Q80 44 154 46 L154 87 L0 87 Z" fill="var(--charcoal)"/>
      <path d="M0 47 Q80 41 154 43" fill="none" stroke="var(--brand-blue)" stroke-width="2"/>
      <path d="M126 46 L131 52 L136 46 Z" fill="#fff"/>
    </svg>
    <p class="contact"><i></i>01-555-0182<br><i></i>info@numbryx.com<br><i></i>www.numbryx.com</p>
    <p class="holder">CIARA MOLLOY<small>Managing Partner</small></p>
  </section>

  <section class="piece card-back on-dark" aria-label="Business card back">
    <div class="decor-wash" role="img" aria-label="Faint brand symbol watermark"></div>
    <div class="wordmark"><span class="dot"></span>Numbryx</div>
  </section>

  <section class="piece slip light-paper" aria-label="Compliment slip">
    <div class="decor-wash" role="img" aria-label="Faint brand symbol watermark"></div>
    <div class="wordmark"><span class="dot"></span>Numbryx</div>
    <svg class="footer" width="360" height="40" viewBox="0 0 360 40">
      <path d="M0 20 Q170 12 360 22 L360 40 L0 40 Z" fill="var(--charcoal)"/>
      <path d="M0 14 Q170 6 360 18" fill="none" stroke="var(--brand-blue)" stroke-width="3"/>
    </svg>
    <p class="address">Harbour Court, Ringsend, Dublin 4.</p>
  </section>

  <section class="piece envelope light-paper" aria-label="Envelope">
    <svg width="360" height="169" viewBox="0 0 360 169">
      <path d="M0 0 H360 V10 L340 40 H20 L0 10 Z" fill="var(--charcoal)"/>
    </svg>
    <span class="seal-dot"></span>
  </section>

</body>
</html>
```